Heartnight Soiree- The Velvet Evening

This is an elegant Dinner concert event for Valentines day February 14 2020 in Vancouver WA. Live R&B band.

Join us for an Evening of live R&B music Featuring some of Oregon and Washington's talented music artists

Tickets prices: $30 concert only pp
$60 dinner and concert pp
$90 VIP Dinner & one drink/Concert/Premium Seating/Special Gift pp
Doors open @ 6:45 Event is 7:30 to 10:30
Location: Lanternfly
417 Hollis St.B Vancouver, WA 98662

www.thekestrelhouse.example for more info.

Target Market(s)

Adults /Couples

Industry/Entity Type

Entertainment Industry

Font styles to use
Sans Serif
Decorative

Colors

Designer to choose colors to be used in the design.

Requirements
Must have
• Add the logos for Sponsors of the Event. Marlows is the main sponsor of the event.
• Main colors should be Red and right for valentine. Needs to be sized for a 5x7 Flyer
• Include the pictures of the Music Artists

```html
<!DOCTYPE html>
<html lang="en">
<head>
<meta charset="utf-8">
<title>Heartnight Soiree - The Velvet Evening</title>
<link rel="stylesheet" href="https://fonts.googleapis.com/css2?family=Great+Vibes&family=Oswald:wght@400;500;700&display=swap">
<style>
  :root {
    --bg-deep: #1a0003;
    --bg-mid: #6e0008;
    --bg-glow: #d8101e;
    --gold-light: #fff0b8;
    --gold: #e3b856;
    --gold-dark: #a87420;
    --accent-red: #ff2a3a;
    --text-white: #ffffff;
    --ring: #140002;
  }
  * { box-sizing: border-box; margin: 0; padding: 0; }
  html, body { width: 1200px; height: 1200px; overflow: hidden; background: var(--bg-deep); }
  .flyer {
    position: relative;
    width: 1200px; height: 1200px; overflow: hidden;
    font-family: "Oswald", sans-serif;
    color: var(--text-white);
    background:
      radial-gradient(ellipse 520px 420px at 620px 520px, var(--bg-glow) 0%, rgba(216,16,30,0.55) 40%, rgba(110,0,8,0) 75%),
      radial-gradient(circle at 50% 45%, var(--bg-mid) 0%, #3a0004 60%, var(--bg-deep) 100%);
  }
  .flourish-field { position: absolute; inset: 0; }
  .gold-text {
    background: linear-gradient(180deg, var(--gold-light) 0%, var(--gold) 45%, var(--gold-dark) 100%);
    -webkit-background-clip: text; background-clip: text; color: transparent;
  }
  .tagline {
    position: absolute; right: 68px; top: 40px; text-align: right;
    color: var(--accent-red); font-weight: 700; font-size: 27px; line-height: 37px; letter-spacing: 1px;
  }
  .title { position: absolute; left: 70px; top: 30px; font-family: "Great Vibes", cursive; font-weight: 400; line-height: 1; z-index: 1; }
  .title span { display: block; white-space: nowrap; }
  .title .line-1 { font-size: 136px; }
  .title .line-2 { font-size: 136px; margin-left: 40px; margin-top: -12px; }
  .title .line-3 { font-size: 76px; margin-left: 10px; margin-top: 4px; }
  .intro { position: absolute; left: 70px; top: 450px; font-size: 31px; font-weight: 400; }
  .intro strong { font-weight: 700; letter-spacing: 1px; }
  .tickets { position: absolute; left: 70px; top: 540px; }
  .tickets-heading { font-size: 33px; font-weight: 700; }
  .tickets-heading small { font-size: 24px; font-weight: 400; }
  .price-row { display: flex; align-items: center; margin-top: 6px; }
  .price { display: flex; align-items: center; }
  .price-amount { font-size: 70px; font-weight: 700; line-height: 1; }
  .price-label { font-size: 25px; margin-left: 14px; line-height: 1.2; }
  .price + .price { margin-left: 46px; }
  .details { position: absolute; left: 70px; top: 812px; display: flex; }
  .detail { display: flex; align-items: flex-start; }
  .detail svg { flex: none; margin-right: 14px; }
  .detail-main { font-size: 31px; font-weight: 700; line-height: 1.1; }
  .detail-sub { font-size: 20px; line-height: 1.35; margin-top: 6px; }
  .detail-date { width: 308px; }
  .detail-time { width: 358px; }
  .more-info { position: absolute; left: 70px; top: 944px; display: flex; align-items: center; font-size: 30px; }
  .more-info svg { margin-right: 20px; }
  .more-info a { color: var(--accent-red); font-weight: 700; font-size: 40px; text-decoration: none; margin-left: 14px; }
  .artist-photo { position: absolute; border-radius: 50%; border: 4px solid var(--ring); z-index: 1; }
  .artist-name {
    position: absolute; z-index: 2; font-family: "Great Vibes", cursive; font-size: 42px; line-height: 1; white-space: nowrap;
    color: var(--text-white); text-shadow: 0 2px 4px rgba(0,0,0,0.8);
  }
  .sponsors { position: absolute; left: 0; right: 0; top: 1070px; height: 100px; }
  .sponsor { position: absolute; display: flex; align-items: center; font-family: "Oswald", sans-serif; }
  .sponsor-salon { left: 70px; top: 28px; font-size: 30px; font-weight: 400; color: var(--text-white); }
  .sponsor-main { left: 0; right: 0; justify-content: center; top: 16px; font-size: 52px; font-weight: 700; color: var(--gold); letter-spacing: 2px; }
  .sponsor-cheer { right: 68px; top: 26px; font-size: 36px; font-weight: 700; color: var(--text-white); }
  .sponsor-cheer .mark { width: 40px; height: 40px; border-radius: 50%; background: var(--text-white); margin-right: 12px; }
</style>
</head>
<body>
<main class="flyer">
  <div class="flourish-field" role="img" aria-label="Decorative red swirls, hearts and music-note flourishes across the background" style="background: radial-gradient(ellipse 460px 360px at 640px 500px, rgba(255,40,50,0.35), rgba(255,40,50,0) 70%);"></div>

  <p class="tagline">FEATURING NATIONALLY ACCLAIMED<br>ARTISTS FROM THE PACIFIC NORTHWEST</p>

  <h1 class="title">
    <span class="line-1 gold-text">Heartnight</span>
    <span class="line-2 gold-text">Soiree</span>
    <span class="line-3 gold-text">-The Velvet Evening</span>
  </h1>

  <p class="intro">Join us for an Evening of <strong>LIVE R&amp;B MUSIC</strong></p>

  <section class="tickets">
    <p class="tickets-heading">TICKET PRICE <small>(per person):</small></p>
    <div class="price-row">
      <div class="price"><span class="price-amount gold-text">$30</span><span class="price-label">Concert only</span></div>
      <div class="price"><span class="price-amount gold-text">$60</span><span class="price-label">Dinner/Concert</span></div>
    </div>
    <div class="price-row">
      <div class="price"><span class="price-amount gold-text">$90</span><span class="price-label">VIP Dinner/Drink/Concert/PremiumSeating/<br>SpecialGift</span></div>
    </div>
  </section>

  <section class="artists">
    <div class="artist-photo" role="img" aria-label="Portrait photo of singer Rosalind Vey" style="left:888px; top:105px; width:234px; height:234px; background: radial-gradient(circle at 50% 40%, #a07060, #4a1a14 70%, #1a0605);"></div>
    <div class="artist-photo" role="img" aria-label="Portrait photo of singer Celeste Amari" style="left:691px; top:280px; width:252px; height:252px; background: radial-gradient(circle at 50% 40%, #7a4a36, #2e1810 70%, #120806);"></div>
    <div class="artist-photo" role="img" aria-label="Portrait photo of singer Dorian Pike" style="left:902px; top:391px; width:240px; height:240px; background: radial-gradient(circle at 50% 45%, #6a4030, #2a2a34 70%, #101018);"></div>
    <div class="artist-photo" role="img" aria-label="Portrait photo of singer Marcus Lendell" style="left:726px; top:520px; width:248px; height:248px; background: radial-gradient(circle at 50% 40%, #7a5040, #3a3638 70%, #c8c4c0);"></div>
    <span class="artist-name" style="left:920px; top:296px;">Rosalind Vey</span>
    <span class="artist-name" style="left:713px; top:462px;">Celeste Amari</span>
    <span class="artist-name" style="left:945px; top:562px;">Dorian Pike</span>
    <span class="artist-name" style="left:784px; top:703px;">Marcus Lendell</span>
  </section>

  <section class="details">
    <div class="detail detail-date">
      <svg width="46" height="46" viewBox="0 0 46 46" aria-hidden="true">
        <rect x="3" y="7" width="40" height="36" rx="3" fill="var(--gold)"/>
        <rect x="3" y="7" width="40" height="9" fill="var(--gold-dark)"/>
        <rect x="11" y="2" width="5" height="10" rx="2" fill="var(--gold)"/>
        <rect x="30" y="2" width="5" height="10" rx="2" fill="var(--gold)"/>
        <g fill="var(--bg-mid)">
          <rect x="8" y="20" width="6" height="5"/><rect x="17" y="20" width="6" height="5"/><rect x="26" y="20" width="6" height="5"/><rect x="35" y="20" width="4" height="5"/>
          <rect x="8" y="28" width="6" height="5"/><rect x="17" y="28" width="6" height="5"/><rect x="26" y="28" width="6" height="5"/><rect x="35" y="28" width="4" height="5"/>
          <rect x="8" y="36" width="6" height="4"/><rect x="17" y="36" width="6" height="4"/>
        </g>
      </svg>
      <div><p class="detail-main">FEBRUARY 14</p><p class="detail-sub">2020, Friday</p></div>
    </div>
    <div class="detail detail-time">
      <svg width="46" height="46" viewBox="0 0 46 46" aria-hidden="true">
        <circle cx="23" cy="23" r="19" fill="none" stroke="var(--gold)" stroke-width="4"/>
        <path d="M23 11 V24 H33" fill="none" stroke="var(--gold)" stroke-width="4" stroke-linecap="round"/>
      </svg>
      <div><p class="detail-main">7:30PM - 10:30PM</p><p class="detail-sub">Doors open @ 6:45pm<br>Concert starts @ 7:30pm</p></div>
    </div>
    <div class="detail detail-venue">
      <svg width="38" height="50" viewBox="0 0 38 50" aria-hidden="true">
        <path d="M19 2 C9 2 2 9.5 2 19 C2 31 19 48 19 48 C19 48 36 31 36 19 C36 9.5 29 2 19 2 Z" fill="none" stroke="var(--gold)" stroke-width="4"/>
        <circle cx="19" cy="19" r="6" fill="var(--gold)"/>
      </svg>
      <div><p class="detail-main">LANTERNFLY</p><p class="detail-sub">417 Hollis St.B Vancouver, WA 98662</p></div>
    </div>
  </section>

  <p class="more-info">
    <svg width="40" height="40" viewBox="0 0 40 40" aria-hidden="true">
      <circle cx="20" cy="20" r="19" fill="var(--gold)"/>
      <circle cx="20" cy="11" r="3" fill="var(--bg-mid)"/>
      <rect x="17" y="17" width="6" height="15" rx="1" fill="var(--bg-mid)"/>
    </svg>
    For more info and to purchase tickets: <a href="#">WWW.THEKESTRELHOUSE.EXAMPLE</a>
  </p>

  <footer class="sponsors">
    <div class="sponsor sponsor-salon">The Ivory Bloom Salon Spa</div>
    <div class="sponsor sponsor-main">MARLOWS</div>
    <div class="sponsor sponsor-cheer"><span class="mark"></span>CHEERWELL</div>
  </footer>
</main>
</body>
</html>
```